VORNAK (PTY)LTD Website design

WEBSITE design based on our different divisions in our organization.
Our company specializes in the following.
Construction
Property development
Demolition
Mining
Transport
Manufacturing of concrete bricks and blocks
Lightweight concrete Readymix
I want a very modern website and look that fits in with our organization and the changing times of the world.
The website must be very professional and crisp and should appeal to both the younger generation and older generation of business leaders and.
The website must be very user friendly and easy to navigate, simple yet modern, professional and corporate.

```html
<!DOCTYPE html>
<html lang="en">
<head>
<meta charset="utf-8">
<title>VORNAK (PTY)LTD</title>
<link href="https://fonts.googleapis.com/css2?family=Open+Sans:wght@300;400;600;700&display=swap" rel="stylesheet">
<style>
:root{
  --blue:#1e6fb8;
  --sky:#29aae1;
  --accent:#2b9bd6;
  --navy:#0f4d7d;
  --btn:#2a74d9;
  --dark:#2a3340;
  --light:#f2f2f2;
  --text:#555;
  --white:#fff;
}
*{margin:0;padding:0;box-sizing:border-box}
html,body{width:1200px;height:1200px;overflow:hidden;background:var(--white)}
body{font-family:'Open Sans',sans-serif;position:relative}
.page{position:absolute;left:311px;top:0;width:722px;height:1500px;transform:scale(.8);transform-origin:0 0;background:var(--white)}
.abs{position:absolute}
.topbar{left:0;top:0;width:722px;height:19px;background:var(--blue);color:var(--white);font-size:7.5px;font-weight:600}
.topbar .item{position:absolute;top:5px;display:flex;align-items:center;gap:3px;white-space:nowrap}
.social-dot{position:absolute;top:6px;width:7px;height:7px;border-radius:50%;background:var(--white)}
.header{top:19px;left:0;width:722px;height:38px}
.brand{left:97px;top:8px;font-size:22px;font-weight:700;color:var(--blue);letter-spacing:.5px}
.nav{top:16px;font-size:7.5px;color:#333}
.nav.active{color:var(--blue)}
.hero{left:0;top:57px;width:722px;height:283px;background:linear-gradient(110deg,#3a3a36 0%,#5a5348 45%,#7a6a55 65%,#b9581d 85%,#4a4640 100%)}
.hero-title-light{left:96px;top:150px;font-size:23px;font-weight:300;color:var(--white);letter-spacing:-.5px}
.hero-title-bold{left:96px;top:172px;font-size:27px;font-weight:700;color:var(--white);letter-spacing:-1px}
.hero-text{left:96px;top:213px;width:320px;font-size:6.8px;line-height:8.5px;color:var(--white)}
.btn-hero{left:96px;top:247px;width:78px;height:23px;background:var(--sky);border:1px solid #bfe6f7;color:var(--white);font-size:10px;display:flex;align-items:center;justify-content:center}
.slide-arrow{top:192px;width:11px;height:14px;background:rgba(0,0,0,.45);color:var(--white);font-size:8px;display:flex;align-items:center;justify-content:center}
.band{left:0;top:340px;width:722px;height:50px;background:var(--sky)}
.band-title{left:97px;top:349px;font-size:15px;font-weight:700;color:var(--white);letter-spacing:-.5px}
.band-sub{left:97px;top:367px;font-size:8.5px;color:var(--white)}
.btn-quote{left:548px;top:355px;width:77px;height:23px;background:var(--navy);color:var(--white);font-size:10px;font-weight:600;display:flex;align-items:center;justify-content:center}
.sec-head{left:96px;padding-left:7px;border-left:4px solid var(--accent)}
.sec-head .kicker{font-size:8px;color:#333;line-height:9px}
.sec-head .title{font-size:18px;font-weight:700;color:var(--blue);line-height:20px;letter-spacing:-.5px}
.sec-head.on-dark .kicker{color:var(--white);font-size:10px;line-height:12px;font-weight:300}
.sec-head.on-dark .title{color:var(--sky)}
.service-photo{left:96px;top:457px;width:187px;height:248px;border:2px solid var(--blue);background:linear-gradient(160deg,#dfeefa 0%,#7fb0e0 35%,#2a5fa8 65%,#0e2c5e 100%)}
.card{width:167px;height:122px;border:1px solid #9cc9ea;text-align:center}
.card svg{display:block;margin:10px auto 0}
.card h3{font-size:12.5px;font-weight:400;color:var(--accent);line-height:13px;margin-top:2px}
.card p{font-size:6.5px;line-height:8px;color:var(--text);margin:6px 5px 0}
.card .btn-read{position:absolute;left:47px;bottom:6px;width:71px;height:20px;background:var(--navy);color:var(--white);font-size:8.5px;font-weight:600;display:flex;align-items:center;justify-content:center}
.steps{left:0;top:728px;width:722px;height:244px;background:linear-gradient(180deg,#4a4541 0%,#3b3835 60%,#2f3a3c 100%)}
.steps-text{left:96px;top:826px;width:535px;font-size:6.8px;line-height:10.8px;color:var(--white)}
.btn-step{top:888px;width:80px;height:22px;background:#1e8ad6;color:var(--white);font-size:6px;display:flex;align-items:center;justify-content:center}
.news{left:0;top:972px;width:722px;height:293px;background:var(--light)}
.news-intro{left:300px;top:1006px;width:330px;font-size:6.8px;line-height:10px;color:#444}
.news-photo{top:1057px;width:159px;height:96px}
.news-card{top:1133px;width:147px;height:102px;background:var(--white);border:1px solid #9cc9ea;text-align:center}
.news-card h3{font-size:11.5px;font-weight:400;color:var(--blue);margin-top:16px;line-height:13px}
.news-card p{font-size:6.3px;line-height:9px;color:var(--text);margin:3px 8px 0}
.news-card .btn-sm{position:absolute;left:40px;top:77px;width:58px;height:15px;background:var(--btn);color:var(--white);font-size:4.5px;display:flex;align-items:center;justify-content:center}
.round-arrow{top:1106px;width:18px;height:18px;border-radius:50%;background:#222;color:var(--white);font-size:9px;display:flex;align-items:center;justify-content:center}
.footer{left:0;top:1265px;width:722px;height:208px;background:var(--dark)}
.foot-head{top:1290px;padding-left:10px;border-left:4px solid var(--white);font-size:15.5px;color:var(--sky);line-height:18px}
.foot-text{font-size:6.8px;line-height:10px;color:var(--white)}
.date{width:20px;height:24px;background:var(--accent);color:var(--white);text-align:center;font-size:11px;font-weight:700;line-height:12px}
.date span{display:block;font-size:7px;font-weight:600;line-height:9px}
.foot-link{font-size:6.5px;color:var(--sky)}
.foot-label{font-size:8px;color:var(--sky)}
.copyright{left:0;top:1473px;width:722px;height:27px;background:var(--blue);color:var(--white);font-size:7px;display:flex;align-items:center;justify-content:center}
</style>
</head>
<body>
<div class="page">
  <div class="abs topbar">
    <div class="item" style="left:97px"><svg width="8" height="8" viewBox="0 0 10 10"><path d="M2 1l2 2-1 1.5c.7 1.3 1.3 1.9 2.5 2.5L7 6l2 2-1.3 1.3C4.5 9 1 5.5.7 2.3z" fill="#fff"/></svg>(+00) 555 010 234</div>
    <div class="item" style="left:178px"><svg width="9" height="7" viewBox="0 0 9 7"><rect width="9" height="7" fill="#fff"/><path d="M0 0l4.5 4L9 0" stroke="#1e6fb8" fill="none"/></svg>contact@vornak.example</div>
    <div class="item" style="left:292px"><svg width="8" height="8" viewBox="0 0 8 8"><path d="M0 1l2.5-1 3 1L8 0v7l-2.5 1-3-1L0 8z" fill="#fff"/></svg>LOREM IPSUM IS SIMPLY DUMMY</div>
    <div class="social-dot" style="left:585px"></div>
    <div class="social-dot" style="left:601px"></div>
    <div class="social-dot" style="left:617px"></div>
  </div>

  <div class="abs header">
    <div class="abs brand">VORNAK</div>
    <div class="abs nav active" style="left:346px">HOME</div>
    <div class="abs nav" style="left:404px">ABOUT</div>
    <div class="abs nav" style="left:465px">SERVICES</div>
    <div class="abs nav" style="left:534px">BLOG</div>
    <div class="abs nav" style="left:591px">CONTACT</div>
  </div>

  <div class="abs hero" role="img" aria-label="Construction worker in hard hat and orange safety vest on a building site"></div>
  <div class="abs slide-arrow" style="left:2px">‹</div>
  <div class="abs slide-arrow" style="left:709px">›</div>
  <div class="abs hero-title-light">CONSTRUCTION</div>
  <div class="abs hero-title-bold">SERVICES PROVIDER</div>
  <div class="abs hero-text">Lorem Ipsum is simply dummy text of the printing and typesetting industry. Lorem Ipsum has been the industry's standard dummy text ever since the 1500s, when an unknown printer took...</div>
  <div class="abs btn-hero">BUILD NOW!</div>

  <div class="abs band"></div>
  <div class="abs band-title">BEST SERVICES &amp; SOLUTIONS:</div>
  <div class="abs band-sub">Quality is what we pursue, We know what we do</div>
  <div class="abs btn-quote">GET A QUOTE</div>

  <div class="abs sec-head" style="top:411px"><div class="kicker">WE ARE EXPERT IN</div><div class="title">SERVICES</div></div>

  <div class="abs service-photo" role="img" aria-label="Glass office tower seen from below against blue sky"></div>

  <div class="abs card" style="left:288px;top:457px">
    <svg width="22" height="22" viewBox="0 0 22 22"><path d="M3 19L15 7M15 7l3-4 2 2-4 3M4 3l5 5-2 2-5-5zM10 12l7 7-2 2-7-7" stroke="#2b9bd6" stroke-width="2.2" fill="none"/></svg>
    <h3>CONSTRUCTION</h3>
    <p>Lorem Ipsum is simply dummy text of the printing and typesetting industry. Lorem Ipsum has been the industry's standard dummy...</p>
    <div class="btn-read">READ MORE</div>
  </div>
  <div class="abs card" style="left:458px;top:457px">
    <svg width="34" height="22" viewBox="0 0 34 22"><rect x="2" y="15" width="18" height="5" rx="2.5" stroke="#2b9bd6" stroke-width="1.5" fill="none"/><rect x="4" y="8" width="12" height="7" stroke="#2b9bd6" stroke-width="1.5" fill="none"/><path d="M16 10L26 3l5 8" stroke="#2b9bd6" stroke-width="1.8" fill="none"/><circle cx="31" cy="13" r="2" fill="#2b9bd6"/></svg>
    <h3>DEMOLITION</h3>
    <p>Lorem Ipsum is simply dummy text of the printing and typesetting industry. Lorem Ipsum has been the industry's standard dummy...</p>
    <div class="btn-read">READ MORE</div>
  </div>
  <div class="abs card" style="left:288px;top:581px">
    <svg width="28" height="26" viewBox="0 0 28 26"><path d="M4 6c6-5 14-5 20 0M14 4l-6 16" stroke="#2b9bd6" stroke-width="2" fill="none"/><path d="M4 24l6-7 5 3 4-4 6 8z" stroke="#2b9bd6" stroke-width="1.5" fill="none"/></svg>
    <h3>MINING</h3>
    <p>Lorem Ipsum is simply dummy text of the printing and typesetting industry. Lorem Ipsum has been the industry's standard dummy...</p>
    <div class="btn-read">READ MORE</div>
  </div>
  <div class="abs card" style="left:458px;top:581px">
    <svg width="28" height="20" viewBox="0 0 28 20" style="margin-top:8px"><path d="M4 10l9-8 9 8M7 9v9h12V9" stroke="#2b9bd6" stroke-width="1.6" fill="none"/><circle cx="8" cy="16" r="3.5" stroke="#2b9bd6" stroke-width="1.5" fill="#fff"/><rect x="19" y="11" width="7" height="7" stroke="#2b9bd6" stroke-width="1.5" fill="none"/></svg>
    <h3>PROPERTY<br>DEVELOPMENT</h3>
    <p>Lorem Ipsum is simply dummy text of the printing and typesetting industry. Lorem Ipsum has been the industry's standard dummy...</p>
    <div class="btn-read">READ MORE</div>
  </div>

  <div class="abs steps" role="img" aria-label="Workers in hard hats among steel reinforcement bars on a construction site, darkened"></div>
  <div class="abs sec-head on-dark" style="top:780px"><div class="kicker">VIRTUALLY BUILD YOUR</div><div class="title">HOUSE IN FEW STEPS</div></div>
  <div class="abs steps-text">Lorem Ipsum is simply dummy text of the printing and typesetting industry. Lorem Ipsum has been the industry's standard dummy text ever since the 1500s, when an unknown printer took a galley of type and scrambled it to make a type specimen book. It has survived not only five centuries, but also the leap into electronic typesetting, remaining essentially unchanged. It was popularised in the 1960s with the release of Norvel sheets containing Lorem Ipsum passages, and more recently with desktop publishing software like Quillset Pagewright including versions of Lorem Ipsum.</div>
  <div class="abs btn-step" style="left:96px">BUILD NOW</div>
  <div class="abs btn-step" style="left:183px">READ MORE</div>

  <div class="abs news"></div>
  <div class="abs sec-head" style="top:1003px"><div class="kicker">LATEST NEWS</div><div class="title">TIPS FROM US</div></div>
  <svg class="abs" style="left:277px;top:1010px" width="14" height="11" viewBox="0 0 14 11"><path d="M0 3h7V0l7 5.5L7 11V8H0z" fill="#1e6fb8"/></svg>
  <div class="abs news-intro">Lorem Ipsum is simply dummy text of the printing and typesetting industry. Lorem Ipsum has been the industry's standard dummy text ever since the 1500s...</div>

  <div class="abs round-arrow" style="left:55px">‹</div>
  <div class="abs round-arrow" style="left:646px">›</div>

  <div class="abs news-photo" style="left:97px;background:linear-gradient(180deg,#6fa8dc 0%,#d9a55a 45%,#a0522d 100%)" role="img" aria-label="Timber roof framing on a house under construction"></div>
  <div class="abs news-photo" style="left:281px;background:linear-gradient(180deg,#8a7a5c 0%,#5f7a84 50%,#3d4a50 100%)" role="img" aria-label="Aerial view of workers on a rebar deck during renovation"></div>
  <div class="abs news-photo" style="left:465px;background:linear-gradient(180deg,#f0ece6 0%,#c9a08a 55%,#8a5a48 100%)" role="img" aria-label="Scaffolding grid with workers against a pale sky"></div>

  <div class="abs news-card" style="left:103px">
    <h3>CONSTRUCTION</h3>
    <p>Lorem Ipsum is simply dummy text of the printing and typesetting industry. Lorem Ipsum has been the industry's standard dummy text ever since...</p>
    <div class="btn-sm">READ MORE</div>
  </div>
  <div class="abs news-card" style="left:287px">
    <h3>RENOVATION</h3>
    <p>Lorem Ipsum is simply dummy text of the printing and typesetting industry. Lorem Ipsum has been the industry's standard dummy text ever since...</p>
    <div class="btn-sm">READ MORE</div>
  </div>
  <div class="abs news-card" style="left:471px">
    <h3>ARCHITECTURAL</h3>
    <p>Lorem Ipsum is simply dummy text of the printing and typesetting industry. Lorem Ipsum has been the industry's standard dummy text ever since...</p>
    <div class="btn-sm">READ MORE</div>
  </div>

  <div class="abs footer"></div>
  <div class="abs foot-head" style="left:97px">ABOUT US</div>
  <div class="abs foot-text" style="left:97px;top:1324px;width:150px">Lorem Ipsum is simply dummy text of the printing and typesetting industry. Lorem Ipsum has been the industry's standard dummy text ever since the 1500s, when an unknown printer took a galley of type and scrambled it to make a type specimen book.</div>
  <div class="abs" style="left:97px;top:1400px;width:14px;height:14px;border-radius:50%;background:var(--btn)"></div>
  <div class="abs" style="left:119px;top:1400px;width:14px;height:14px;border-radius:50%;background:var(--accent)"></div>

  <div class="abs foot-head" style="left:275px">LATEST NEWS</div>
  <div class="abs date" style="left:276px;top:1326px">18<span>Dec</span></div>
  <div class="abs foot-text" style="left:301px;top:1324px;width:140px">Lorem Ipsum is simply dummy text of the printing and typesetting industry. Lorem Ipsum has been...</div>
  <div class="abs foot-link" style="left:301px;top:1360px">READ MORE...</div>
  <div class="abs date" style="left:276px;top:1385px">18<span>Dec</span></div>
  <div class="abs foot-text" style="left:301px;top:1383px;width:140px">Lorem Ipsum is simply dummy text of the printing and typesetting industry. Lorem Ipsum has been...</div>
  <div class="abs foot-link" style="left:301px;top:1419px">READ MORE...</div>

  <div class="abs foot-head" style="left:465px">GET IN TOUCH</div>
  <div class="abs foot-label" style="left:465px;top:1320px">ADDRESS:</div>
  <div class="abs foot-text" style="left:465px;top:1334px;width:150px">Lorem Ipsum is simply dummy text of the printing and typesetting industry.</div>
  <div class="abs foot-label" style="left:465px;top:1364px">PHONE:</div>
  <div class="abs" style="left:465px;top:1378px;font-size:13px;color:var(--white)">(+00) 555 010 234</div>
  <div class="abs foot-label" style="left:465px;top:1406px">EMAIL:</div>
  <div class="abs" style="left:465px;top:1421px;font-size:7px;font-weight:600;color:var(--white)">CONTACT@VORNAK.EXAMPLE</div>

  <div class="abs copyright">© 2018 vornak.example. All Rights Reserved.</div>
</div>
</body>
</html>
```